Thrifty Haul: Junk Removal - Website Design

We need a design and uploaded to Hostivra.com. I enclosed our postcard for reference too. I need a contact from at the top right so I can get leads.

Here are the sites I like:

https://trykemvan.com/
https://www.1800zibwaste.com
https://www.brindlemoversclearingco.com/junk-removal/
http://anookforgrams.com/
http://www.drivelunt.com/alternate/
https://www.servicevangifting.org/
http://www.autosforpatriots.org/indexj/

Coding

Coded - Design and coding required

Number of Pages Required

1 page

```html
<!DOCTYPE html>
<html lang="en">
<head>
<meta charset="utf-8">
<title>Thrifty Haul – Junk Removal</title>
<link href="https://fonts.googleapis.com/css2?family=Montserrat:wght@700&family=Raleway:wght@400;500;600&family=Roboto+Slab:wght@400;600;700&display=swap" rel="stylesheet">
<style>
:root{
  --green:#7abf2c;
  --green-dark:#5f9e1c;
  --blue:#0f3286;
  --ink:#1c3a78;
  --text:#5b5b5b;
  --footer:#1e1e1e;
  --white:#ffffff;
}
*{box-sizing:border-box;margin:0;padding:0}
html,body{width:1200px;height:4471px;overflow:hidden}
body{position:relative;background:var(--white);font-family:'Raleway',sans-serif;color:var(--text)}
.abs{position:absolute}
.btn{position:absolute;background:var(--green);color:var(--white);font-family:'Roboto Slab',serif;font-weight:700;font-size:15px;display:flex;align-items:center;justify-content:center;letter-spacing:.3px}

/* header */
.brand{position:absolute;font-family:'Montserrat',sans-serif;font-weight:700;color:var(--green);letter-spacing:.5px;font-size:40px;line-height:48px}
.header-brand{left:110px;top:18px}
.header-phone{right:75px;top:24px;font-family:'Montserrat',sans-serif;font-weight:700;font-size:25px;color:var(--blue);display:flex;align-items:center;gap:10px}
.main-nav{left:0;top:104px;width:1200px;height:52px;background:var(--blue)}
.main-nav ul{list-style:none;display:flex;position:absolute;left:93px;top:0;height:52px}
.main-nav li{color:var(--white);font-family:'Roboto Slab',serif;font-size:13px;padding:0 15px;display:flex;align-items:center}
.main-nav li.active{background:var(--green)}

/* hero */
.hero{left:0;top:156px;width:1200px;height:556px;background:linear-gradient(100deg,#5a3a26 0%,#7a4a2a 30%,#b46a2c 50%,#6f6f72 70%,#b07a3a 100%)}
.hero-title{left:110px;top:330px;font-family:'Roboto Slab',serif;font-weight:700;font-size:66px;line-height:80px;color:var(--white)}
.hero-copy{left:111px;top:410px;width:520px;font-size:15px;line-height:27px;color:var(--white)}
.hero-dots{left:542px;top:678px;display:flex;gap:12px;align-items:center}
.hero-dots span{width:9px;height:9px;border-radius:50%;background:var(--green)}
.hero-dots span.on{width:18px;height:18px;background:transparent;border:2px solid var(--green);position:relative}
.hero-dots span.on::after{content:"";position:absolute;left:3px;top:3px;width:8px;height:8px;border-radius:50%;background:var(--green)}

.quote-form{left:730px;top:76px;width:359px;height:384px}
.quote-head{position:absolute;left:0;top:0;width:359px;height:115px;background:var(--green);color:var(--white);font-family:'Roboto Slab',serif;font-size:22px;line-height:34px;text-align:center;padding-top:24px}
.quote-body{position:absolute;left:0;top:115px;width:359px;height:269px;background:var(--blue)}
.field{position:absolute;background:var(--white);height:42px;font-size:13px;color:#666;padding:14px 0 0 12px}
.fold-l,.fold-r{position:absolute;top:76px;width:0;height:0;border-bottom:24px solid var(--green-dark)}
.fold-l{left:712px;border-left:18px solid transparent}
.fold-r{left:1089px;border-right:18px solid transparent}

/* who we are */
.section-title{font-family:'Roboto Slab',serif;font-weight:700;color:var(--ink)}
.who-title{left:111px;top:842px;font-size:40px}
.who-title b{color:var(--green);font-weight:700}
.who-copy{left:111px;top:910px;width:495px;font-size:15px;line-height:34.5px;text-align:justify}
.who-photo{left:637px;top:816px;width:452px;height:469px;background:linear-gradient(160deg,#7fbf3a,#5e9b2a 70%,#1e3f95 100%)}

/* services */
.services{left:0;top:1390px;width:1200px;height:827px;background:var(--blue)}
.services-title{left:0;top:1450px;width:1200px;text-align:center;font-size:40px;color:var(--white)}
.services-sub{left:0;top:1524px;width:1200px;text-align:center;color:var(--white);font-size:15px;line-height:34px}
.tile{position:absolute;width:316px;height:256px;display:flex;align-items:center;justify-content:center;text-align:center;color:var(--white);font-family:'Roboto Slab',serif;font-weight:700;font-size:21px;line-height:34px}

/* process */
.process-title{left:0;top:2320px;width:1200px;text-align:center;font-size:40px}
.process-art{left:190px;top:2390px;width:860px;height:390px;background:linear-gradient(180deg,#f4f4f4,#e6e6e6)}
.worker-left{left:0;top:2240px;width:220px;height:634px;background:linear-gradient(180deg,#2a4fbf,#1d3ea8)}
.hex{position:absolute;width:180px;height:208px;background:var(--green);clip-path:polygon(50% 0,100% 25%,100% 75%,50% 100%,0 75%,0 25%);display:flex;align-items:center;justify-content:center;text-align:center;color:var(--white);font-family:'Roboto Slab',serif;font-weight:700;font-size:15px;line-height:28px}

/* junk removal band */
.band{left:0;top:2849px;width:1200px;height:500px;background:linear-gradient(180deg,#3b4a6c,#25324f)}
.band-banner{left:386px;top:2843px;width:814px;height:115px;background:var(--blue);clip-path:polygon(100px 0,100% 0,100% 100%,0 100%)}
.band-title{left:500px;top:2862px;width:700px;text-align:center;color:var(--white);font-family:'Roboto Slab',serif;font-weight:700;font-size:58px;line-height:76px}
.card{position:absolute;top:3019px;width:320px;height:259px;background:var(--white);border-radius:3px;text-align:center}
.card svg{margin-top:44px}
.card p{font-family:'Roboto Slab',serif;font-weight:600;font-size:15px;line-height:28px;color:var(--blue);margin-top:12px}
.badge{left:992px;top:2975px;width:156px;height:156px;border-radius:50%;background:var(--white);border:6px solid var(--blue);display:flex;flex-direction:column;align-items:center;justify-content:center;text-align:center}
.badge strong{font-family:'Roboto Slab',serif;font-weight:700;font-size:30px;line-height:32px;color:var(--green)}
.badge em{font-style:normal;font-family:'Roboto Slab',serif;font-weight:700;font-size:16px;line-height:20px;color:var(--blue)}
.badge small{font-weight:600;font-size:9px;line-height:11px;color:#222;margin-top:2px}

/* why choose */
.why-title{left:111px;top:3440px;font-size:32px;color:#222}
.why-title b{color:var(--green);font-weight:700}
.why-lead{left:111px;top:3497px;width:470px;font-size:15px;line-height:27px}
.reason{position:absolute;left:111px;width:400px;height:80px}
.reason .ico{position:absolute;left:0;top:0;width:66px;height:66px;border-radius:50%;border:2px solid #b9c4df;display:flex;align-items:center;justify-content:center}
.reason .ico i{width:50px;height:50px;border-radius:50%;background:var(--blue);display:block}
.reason h3{position:absolute;left:79px;top:0;font-family:'Roboto Slab',serif;font-weight:600;font-size:15px;color:#222}
.reason p{position:absolute;left:79px;top:28px;width:290px;font-size:12.5px;line-height:24px;color:#777}
.pic{position:absolute;box-shadow:0 4px 14px rgba(0,0,0,.25)}

/* footer */
.site-footer{left:0;top:4085px;width:1200px;height:386px;background:var(--footer)}
.footer-brand{left:110px;top:4192px}
.socials{left:110px;top:4260px;display:flex;gap:16px}
.socials span{width:20px;height:20px;background:var(--white);border-radius:3px}
.foot-contact{left:110px;font-family:'Montserrat',sans-serif;color:var(--white);display:flex;align-items:center;gap:12px}
.foot-col{position:absolute;top:4132px}
.foot-col h4{font-family:'Roboto Slab',serif;font-weight:400;font-size:21px;color:var(--green);margin-bottom:12px}
.foot-col li{list-style:none;color:var(--white);font-size:13px;line-height:34px;padding-left:5px}
.copyright{left:0;top:4421px;width:1200px;text-align:center;color:var(--white);font-size:13px}
</style>
</head>
<body>

<header>
  <div class="brand header-brand">THRIFTY HAUL</div>
  <div class="abs header-phone">
    <svg width="20" height="20" viewBox="0 0 20 20"><rect width="20" height="20" rx="4" fill="#0f3286"/><path d="M6 4l2.5 0 1 3-1.5 1.2a8 8 0 0 0 3.8 3.8L13 10.5l3 1V14a2 2 0 0 1-2 2A10 10 0 0 1 4 6a2 2 0 0 1 2-2z" fill="#fff"/></svg>
    1-800-555-0142
  </div>
  <nav class="abs main-nav">
    <ul>
      <li class="active">HOME</li><li>ABOUT</li><li>SERVICES</li><li>JUNK REMOVAL</li><li>WHY CHOOSE</li><li>ENG ⌄</li>
    </ul>
  </nav>
</header>

<section>
  <div class="abs hero" role="img" aria-label="Junk removal worker in orange high-visibility uniform beside a garbage truck, autumn trees"></div>
  <h1 class="abs hero-title">THRIFTY HAUL</h1>
  <p class="abs hero-copy">Lorem ipsum dolor sit amet, consectetur adipiscing elit, sed do eiusmod tempor incididunt ut labore et dolore magna aliqua.</p>
  <div class="btn" style="left:111px;top:474px;width:155px;height:50px">GET STARTED</div>
  <div class="abs hero-dots"><span></span><span class="on"></span><span></span><span></span></div>

  <div class="fold-l"></div><div class="fold-r"></div>
  <form class="abs quote-form">
    <div class="quote-head">GET FREE QUOTES FROM<br>THRIFTY HAUL</div>
    <div class="quote-body">
      <div class="field" style="left:6px;top:32px;width:170px">First Name</div>
      <div class="field" style="left:182px;top:32px;width:171px">Last Name</div>
      <div class="field" style="left:6px;top:97px;width:170px">Email Address</div>
      <div class="field" style="left:182px;top:97px;width:171px">Phone</div>
      <div class="field" style="left:6px;top:162px;width:347px">State<span style="position:absolute;right:14px;top:13px;font-size:10px;color:#222">▼</span></div>
      <div class="btn" style="left:6px;top:225px;width:176px;height:44px;font-size:14px">GET QUOTE NOW</div>
    </div>
  </form>
</section>

<section>
  <h2 class="abs section-title who-title">WHO WE <b>ARE</b></h2>
  <p class="abs who-copy">Nemo enim ipsam voluptatem quia voluptas sit aspernatur aut odit aut fugit, sed quia consequuntur magni dolores eos qui ratione voluptatem sequi nesciunt. Neque porro quisquam est, qui dolorem ipsum quia dolor sit amet, consectetur, adipisci velit, sed quia non numquam eius modi tempora incidunt ut labore et dolore magnam aliquam quaerat voluptatem. Ut enim ad minima veniam, quis nostrum exercitationem ullam corporis suscipit laboriosam, nisi ut aliquid ex ea commodi consequatur</p>
  <div class="btn" style="left:111px;top:1197px;width:155px;height:50px">READ MORE</div>
  <div class="abs who-photo" role="img" aria-label="Worker in a safety vest holding a broom next to a green wheelie bin on a green backdrop"></div>
</section>

<section>
  <div class="abs services"></div>
  <h2 class="abs section-title services-title">FULL SERVICES JUNK REMOVAL</h2>
  <p class="abs services-sub">Thrifty Haul is a full-service junk removal company areas across the united states.<br>we're in your neighborhood</p>
  <div class="tile" style="left:111px;top:1615px;background:linear-gradient(160deg,#8a7a5a,#4e5a3a)" role="img" aria-label="Family carrying bags of household junk">RESIDENTIAL</div>
  <div class="tile" style="left:441px;top:1615px;background:linear-gradient(160deg,#b89a4a,#7a5a2a)" role="img" aria-label="Moving boxes and old furniture">MOVING</div>
  <div class="tile" style="left:771px;top:1615px;background:linear-gradient(160deg,#d8d8d8,#8a8f9a)" role="img" aria-label="Two workers carrying cardboard in an office">COMMERCIAL JUNK<br>REMOVING</div>
  <div class="tile" style="left:111px;top:1885px;background:linear-gradient(160deg,#4a4a4a,#2a2a2a)" role="img" aria-label="Empty industrial warehouse interior">STORAGE</div>
  <div class="tile" style="left:441px;top:1885px;background:linear-gradient(180deg,#6b7fa6,#5a4f42)" role="img" aria-label="Debris of a collapsed building after a disaster">DISASTER</div>
  <div class="tile" style="left:771px;top:1885px;background:linear-gradient(160deg,#d08a3a,#7a6a5a)" role="img" aria-label="Excavator demolishing a building for renovation">RENOVATION</div>
</section>

<section>
  <div class="abs process-art" role="img" aria-label="Faint line sketch of a garbage truck"></div>
  <div class="abs worker-left" role="img" aria-label="Smiling cleaner in blue overalls holding a mop"></div>
  <h2 class="abs section-title process-title">OUR PROCESS</h2>
  <svg class="abs" style="left:0;top:2200px" width="1200" height="650">
    <g stroke="#1c3a78" stroke-width="1.2">
      <line x1="420" y1="335" x2="460" y2="375"/>
      <line x1="623" y1="375" x2="645" y2="350"/>
      <line x1="825" y1="335" x2="860" y2="375"/>
    </g>
  </svg>
  <div class="hex" style="left:240px;top:2383px">CALL US<br>TODAY</div>
  <div class="hex" style="left:443px;top:2540px">SAME DAY<br>SERVICES</div>
  <div class="hex" style="left:645px;top:2383px">COVID- 19<br>COMAPLIANT</div>
  <div class="hex" style="left:858px;top:2538px">BEST PRICE<br>GUARANTEED</div>
</section>

<section>
  <div class="abs band" role="img" aria-label="Dim photo of sanitation workers at dusk"></div>
  <div class="abs band-banner"></div>
  <h2 class="abs band-title">JUNK REMOVAL</h2>
  <div class="card" style="left:111px">
    <svg width="110" height="100" viewBox="0 0 110 100" fill="none" stroke-width="3">
      <rect x="15" y="50" width="80" height="40" stroke="#7abf2c"/>
      <line x1="15" y1="70" x2="95" y2="70" stroke="#0f3286"/>
      <rect x="30" y="20" width="20" height="30" stroke="#0f3286"/>
      <line x1="80" y1="8" x2="80" y2="50" stroke="#7abf2c"/>
    </svg>
    <p>HOUSE GARAGE ESTATE<br>CLEAN OUT</p>
  </div>
  <div class="card" style="left:439px">
    <svg width="110" height="100" viewBox="0 0 110 100" fill="none" stroke-width="3">
      <rect x="20" y="5" width="45" height="85" stroke="#7abf2c"/>
      <line x1="20" y1="35" x2="65" y2="35" stroke="#7abf2c"/>
      <rect x="40" y="55" width="50" height="35" stroke="#0f3286"/>
      <rect x="46" y="61" width="28" height="23" stroke="#0f3286"/>
    </svg>
    <p>FURNITURE APPLIANCE<br>REMOVAL</p>
  </div>
  <div class="card" style="left:768px">
    <svg width="110" height="100" viewBox="0 0 110 100" fill="none" stroke-width="4" stroke="#7abf2c">
      <path d="M45 15 L55 5 L65 15 M55 5 L75 40"/>
      <path d="M90 60 L80 85 L30 85" stroke="#0f3286"/>
      <path d="M20 75 L40 40 M30 45 L40 40 L43 50"/>
    </svg>
    <p>WE RECYCLE</p>
  </div>
  <div class="abs badge">
    <strong>FREE</strong>
    <em>ESTIMATE</em>
    <small>Provided prior to<br>item removal</small>
  </div>
</section>

<section>
  <h2 class="abs section-title why-title">WHY CHOOSE <b>THRIFTY HAUL</b></h2>
  <p class="abs why-lead">Nemo enim ipsam voluptatem quia voluptas sit aspernatur aut odit aut fugit, sed quia consequuntur magni</p>
  <div class="reason" style="top:3578px"><div class="ico"><i></i></div><h3>ON TIME SERVICE</h3><p>Nemo enim ipsam voluptatem quia voluptas sit aspernatur aut odit aut fugit.</p></div>
  <div class="reason" style="top:3681px"><div class="ico"><i></i></div><h3>UP FRONT PRICING</h3><p>Nemo enim ipsam voluptatem quia voluptas sit aspernatur aut odit aut fugit.</p></div>
  <div class="reason" style="top:3775px"><div class="ico"><i></i></div><h3>FULL SERVICE JUNK REMOVAL</h3><p>Nemo enim ipsam voluptatem quia voluptas sit aspernatur aut odit aut fugit.</p></div>
  <div class="reason" style="top:3877px"><div class="ico"><i></i></div><h3>COVID- 19 COMPLIANT</h3><p>Nemo enim ipsam voluptatem quia voluptas sit aspernatur aut odit aut fugit.</p></div>
  <div class="pic" style="left:782px;top:3474px;width:312px;height:286px;background:linear-gradient(160deg,#b9c3cf,#e07a2a 60%,#8a8f98)" role="img" aria-label="Two workers in orange uniforms in front of a truck"></div>
  <div class="pic" style="left:551px;top:3543px;width:229px;height:334px;background:linear-gradient(160deg,#6a6a6a,#2a2a2a)" role="img" aria-label="Worker lifting black rubbish bags"></div>
  <div class="pic" style="left:677px;top:3700px;width:313px;height:281px;background:linear-gradient(160deg,#4a4f5a,#c0602a 60%,#3a3a3a)" role="img" aria-label="Two workers loading a garbage truck"></div>
</section>

<footer>
  <div class="abs site-footer"></div>
  <div class="brand footer-brand">THRIFTY HAUL</div>
  <div class="abs socials"><span></span><span></span><span></span><span></span></div>
  <div class="abs foot-contact" style="top:4305px;font-size:25px;font-weight:700">
    <svg width="20" height="20" viewBox="0 0 20 20"><rect width="20" height="20" rx="4" fill="#7abf2c"/><path d="M6 4l2.5 0 1 3-1.5 1.2a8 8 0 0 0 3.8 3.8L13 10.5l3 1V14a2 2 0 0 1-2 2A10 10 0 0 1 4 6a2 2 0 0 1 2-2z" fill="#1e1e1e"/></svg>
    1-800-555-0142
  </div>
  <div class="abs foot-contact" style="top:4354px;font-size:20px;font-weight:700">
    <svg width="22" height="16" viewBox="0 0 22 16"><rect width="22" height="16" rx="2" fill="#7abf2c"/><path d="M1 2l10 7 10-7" stroke="#1e1e1e" stroke-width="2" fill="none"/></svg>
    WWW.ThriftyHaul.com
  </div>
  <div class="foot-col" style="left:533px"><h4>SERVICES</h4><ul><li>Residential</li><li>Moving</li><li>Commercial</li><li>Storage</li><li>Disaster</li><li>Renovation</li></ul></div>
  <div class="foot-col" style="left:694px"><h4>OPPORTUNITY</h4><ul><li>Jobs / Careers</li><li>Drive for Kemvan</li><li>Become a Partner</li><li>Partner Portal</li></ul></div>
  <div class="foot-col" style="left:901px"><h4>COMPANY</h4><ul><li>About Us</li><li>Press &amp; Media</li><li>Our Reviews</li><li>Contact Us</li></ul></div>
  <p class="abs copyright">© 2020 All Rights Reserved</p>
</footer>

</body>
</html>
```